Business Card Design with new logo

Warren Peltzman 4175
E 118th Rd Casey, IL 62420
Cell: 217-555-0187
peltzmanrebuilds@mailhollow.com

Classic Car Restoration Services Buy Sell Trade Consign

Contact Information for Business Card

Warren Peltzman 9698
Cell: 217-555-0187

```html
<!DOCTYPE html>
<html lang="en">
<head>
<meta charset="utf-8">
<title>Peltzman Rebuilds LLC – Business Card</title>
<link href="https://fonts.googleapis.com/css2?family=Open+Sans:wght@400;600;700;800&display=swap" rel="stylesheet">
<style>
  :root {
    --bg: #5c5c5c;
    --card: #ffffff;
    --navy: #12222f;
    --red: #ef3e33;
    --red-deep: #c8242a;
    --ink: #1a1a1a;
  }
  * { box-sizing: border-box; margin: 0; padding: 0; }
  html, body {
    width: 1200px; height: 1200px; overflow: hidden;
    background: var(--bg);
    font-family: "Open Sans", sans-serif;
  }
  .card {
    position: absolute; left: 240px; width: 720px; height: 420px;
    background: var(--card); border-radius: 29px; overflow: hidden;
  }
  .card--front { top: 142px; }
  .card--back { top: 638px; }

  /* front */
  .brand {
    position: absolute; display: flex; align-items: center; gap: 12px;
    color: var(--navy); font-weight: 800; letter-spacing: 0.5px;
  }
  .card--front .brand { left: 44px; top: 58px; font-size: 26px; }
  .brand__dot { width: 30px; height: 30px; border-radius: 50%; background: var(--red); flex: none; }
  .address {
    position: absolute; left: 43px; top: 170px;
    font-size: 22px; line-height: 32px; color: var(--ink);
  }
  .contact {
    position: absolute; left: 40px; display: flex; align-items: center; gap: 12px;
    font-size: 17px; color: var(--ink);
  }
  .contact--phone { top: 262px; }
  .contact--email { top: 305px; }
  .contact svg { width: 24px; height: 24px; fill: var(--navy); }
  .person {
    position: absolute; right: 36px; top: 196px; text-align: right;
  }
  .person__name { font-size: 29px; font-weight: 700; color: var(--navy); line-height: 1.2; }
  .person__name span { color: var(--red); }
  .person__title { font-size: 17px; font-weight: 700; color: var(--navy); margin-top: 2px; }
  .band { position: absolute; }
  .band--red-front { left: 0; top: 374px; width: 570px; height: 30px; background: var(--red); }
  .band--navy-front { left: 545px; top: 374px; width: 175px; height: 30px; background: var(--navy);
    clip-path: polygon(8% 0, 100% 0, 100% 100%, 0 100%); }
  .band__email {
    position: absolute; left: 144px; top: 376px; font-size: 17px; color: var(--navy);
  }

  /* back */
  .card--back .brand {
    left: 0; right: 0; top: 110px; flex-direction: column; gap: 16px;
    font-size: 40px;
  }
  .card--back .brand__dot { width: 80px; height: 80px; }
  .tagline {
    position: absolute; left: 0; right: 0; top: 346px; padding-left: 48px;
    text-align: center; font-size: 17px; color: var(--ink);
  }
  .band--navy-back { left: 0; bottom: 0; width: 400px; height: 26px; background: var(--navy);
    clip-path: polygon(0 0, 100% 0, 98.5% 100%, 0 100%); }
  .band--red-back { left: 394px; bottom: 0; width: 326px; height: 26px; background: var(--red-deep);
    clip-path: polygon(2% 0, 100% 0, 100% 100%, 0 100%); }
</style>
</head>
<body>
  <section class="card card--front">
    <div class="brand"><span class="brand__dot"></span>Peltzman Rebuilds LLC</div>
    <p class="address">Warren Peltzman 4175<br>E 118th Rd Casey, IL 62420</p>
    <div class="contact contact--phone">
      <svg viewBox="0 0 24 24" aria-hidden="true"><path d="M6.6 10.8a15.1 15.1 0 0 0 6.6 6.6l2.2-2.2c.3-.3.7-.4 1-.2 1.1.4 2.3.6 3.6.6.6 0 1 .4 1 1V20c0 .6-.4 1-1 1A17 17 0 0 1 3 4c0-.6.4-1 1-1h3.5c.6 0 1 .4 1 1 0 1.3.2 2.5.6 3.6.1.3 0 .7-.2 1z"/></svg>
      <span>217-555-0187</span>
    </div>
    <div class="contact contact--email">
      <svg viewBox="0 0 24 24" aria-hidden="true"><path d="M2 5h20v14H2zm2 2v.4l8 5 8-5V7z"/></svg>
      <span>peltzmanrebuilds@mailhollow.com</span>
    </div>
    <div class="person">
      <div class="person__name">Dorian <span>Kessel</span></div>
      <div class="person__title">CEO and Co-founder</div>
    </div>
    <div class="band band--red-front"></div>
    <div class="band band--navy-front"></div>
    <span class="band__email">peltzmanrebuilds@mailhollow.com</span>
  </section>

  <section class="card card--back">
    <div class="brand"><span class="brand__dot"></span>Peltzman Rebuilds LLC</div>
    <p class="tagline">Classic Car Restoration Services Buy Sell Trade Consign</p>
    <div class="band band--navy-back"></div>
    <div class="band band--red-back"></div>
  </section>
</body>
</html>
```